Ward Compass Business Card Design*

We need a business card design for our company Ward Compass. Our company is specialized in providing online consulting services regarding medical institutions, hospitals and doctors. We work with patients worldwide looking to choose between healthcare providers. We have a website you may use as a reference, where we list doctors and clinics worldwide. So we target Medical providers as well as patients worldwide.
Target Market(s)
Medical Providers and patients around the world
Industry/Entity Type
Medical
Contact Information for Business Card
Salma Derkaoui
CEO
+90 612 348 2071
info@wardcompass-example.com
www.wardcompass-example.com
14 Annakhil 3 H.R.B. Rabat, Morocco
Requirements
Must have
- Company logo/name on one full side, personal info and smaller logo and company name on the other side.
Nice to have
- Smart and elegant design

```html
<!DOCTYPE html>
<html lang="en">
<head>
<meta charset="utf-8">
<title>Ward Compass Business Card</title>
<link href="https://fonts.googleapis.com/css2?family=Lato:wght@400;700&family=Arimo:wght@400;700&display=swap" rel="stylesheet">
<style>
  :root {
    --navy: #123a6b;
    --navy-deep: #0c2b52;
    --ink: #2f3b4a;
    --grey-text: #5b6470;
    --logo-grey: #8c97a6;
    --paper: #ffffff;
    --paper-shade: #e9ebee;
    --backdrop: #2a2a2a;
  }
  * { box-sizing: border-box; margin: 0; padding: 0; }
  html, body { width: 1200px; height: 997px; overflow: hidden; }
  body {
    background: var(--backdrop);
    font-family: "Lato", sans-serif;
    display: flex;
    justify-content: center;
    align-items: center;
    gap: 70px;
  }
  .card {
    position: relative;
    width: 340px;
    height: 580px;
    border-radius: 14px;
    overflow: hidden;
    background: linear-gradient(160deg, var(--paper) 40%, var(--paper-shade));
    box-shadow: 0 18px 40px rgba(0,0,0,.55);
    display: flex;
    flex-direction: column;
  }
  .band {
    background: var(--navy);
    position: relative;
  }
  .band--top { height: 70px; }
  .band--bottom { height: 80px; margin-top: auto; }
  .stripes {
    position: absolute;
    left: 0; right: 0;
    height: 22px;
    background: repeating-linear-gradient(to bottom,
      var(--paper) 0 4px, var(--navy) 4px 9px);
  }
  .band--top .stripes { bottom: 0; }
  .band--bottom .stripes { top: 0; }

  /* logo side */
  .logo-side .body {
    flex: 1;
    display: flex;
    flex-direction: column;
    align-items: center;
    padding-top: 110px;
  }
  .brand {
    display: flex;
    align-items: center;
    gap: 10px;
    font-family: "Lato", sans-serif;
    font-weight: 700;
    letter-spacing: 1px;
    color: var(--logo-grey);
  }
  .brand__dot {
    width: 16px; height: 16px;
    border-radius: 50%;
    background: var(--logo-grey);
  }
  .logo-side .brand { font-size: 28px; }
  .social-list {
    margin-top: 70px;
    list-style: none;
    font-size: 14px;
    line-height: 1.5;
    color: var(--ink);
    align-self: flex-end;
    padding-right: 50px;
  }
  .social-dots {
    position: absolute;
    left: 0; right: 0; bottom: 18px;
    display: flex;
    justify-content: center;
    gap: 8px;
  }
  .social-dots span {
    width: 20px; height: 20px;
    border-radius: 50%;
    background: #3d6fa8;
    border: 1px solid rgba(255,255,255,.5);
  }

  /* personal side */
  .info-side .body {
    flex: 1;
    display: flex;
    flex-direction: column;
    align-items: center;
    padding-top: 20px;
    text-align: center;
  }
  .info-side .brand {
    align-self: flex-end;
    padding-right: 24px;
    font-size: 18px;
    font-weight: 400;
    color: var(--grey-text);
  }
  .info-side .brand__dot { width: 10px; height: 10px; }
  .person { margin-top: 90px; }
  .person__name {
    font-family: "Arimo", sans-serif;
    font-weight: 700;
    font-size: 21px;
    color: var(--navy);
    letter-spacing: .5px;
  }
  .person__role {
    font-family: "Arimo", sans-serif;
    font-weight: 700;
    font-size: 16px;
    color: var(--grey-text);
  }
  .divider {
    width: 170px;
    height: 3px;
    margin: 22px auto;
    background: linear-gradient(90deg, transparent, var(--navy), transparent);
  }
  .icons { display: flex; gap: 14px; justify-content: center; margin-bottom: 8px; }
  .icons svg, .globe { width: 16px; height: 16px; fill: var(--navy); }
  .contact { font-size: 15px; color: var(--ink); line-height: 1.45; }
  .web {
    margin-top: 8px;
    font-family: "Arimo", sans-serif;
    font-size: 16px;
    color: var(--navy);
  }
  .tagline {
    position: absolute;
    left: 0; right: 0; bottom: 18px;
    text-align: center;
    color: var(--paper);
    font-family: "Arimo", sans-serif;
    font-size: 14px;
  }
</style>
</head>
<body>

  <section class="card logo-side">
    <div class="band band--top"><div class="stripes"></div></div>
    <div class="body">
      <div class="brand"><span class="brand__dot"></span>WARD COMPASS</div>
      <ul class="social-list">
        <li>Friendbook/wardcompass</li>
        <li>Chirper/wardcompass</li>
        <li>Linkwork/wardcompass</li>
        <li>Vidstream/wardcompass</li>
        <li>Snapgram/wardcompass</li>
      </ul>
    </div>
    <div class="band band--bottom">
      <div class="stripes"></div>
      <div class="social-dots"><span></span><span></span><span></span><span></span><span></span><span></span></div>
    </div>
  </section>

  <section class="card info-side">
    <div class="band band--top"><div class="stripes"></div></div>
    <div class="body">
      <div class="brand"><span class="brand__dot"></span>WARD COMPASS</div>
      <div class="person">
        <div class="person__name">SALMA DERKAOUI</div>
        <div class="person__role">CEO</div>
      </div>
      <div class="divider"></div>
      <div class="icons">
        <svg viewBox="0 0 24 24" aria-hidden="true"><path d="M6.6 10.8a15 15 0 0 0 6.6 6.6l2.2-2.2a1 1 0 0 1 1-.25 11.4 11.4 0 0 0 3.6.57 1 1 0 0 1 1 1V20a1 1 0 0 1-1 1A17 17 0 0 1 3 4a1 1 0 0 1 1-1h3.5a1 1 0 0 1 1 1c0 1.25.2 2.45.57 3.6a1 1 0 0 1-.25 1z"/></svg>
        <svg viewBox="0 0 24 24" aria-hidden="true"><path d="M2 5h20v14H2z M2 5l10 8 10-8" fill="none" stroke="#123a6b" stroke-width="2"/></svg>
      </div>
      <div class="contact">
        <div>+90 612 348 2071</div>
        <div>info@wardcompass-example.com</div>
      </div>
      <div class="divider"></div>
      <svg class="globe" viewBox="0 0 24 24" aria-hidden="true"><circle cx="12" cy="12" r="10" fill="none" stroke="#123a6b" stroke-width="2"/><path d="M2 12h20M12 2c3 3 3 17 0 20M12 2c-3 3-3 17 0 20" fill="none" stroke="#123a6b" stroke-width="1.6"/></svg>
      <div class="web">www.wardcompass-example.com</div>
    </div>
    <div class="band band--bottom">
      <div class="stripes"></div>
      <div class="tagline">Find &amp; compare top rated clinics world wide</div>
    </div>
  </section>

</body>
</html>
```